New Business Card Design Project

The look of the business cards should include
-Clean Lines
-Should suit a sophisticated customer
-Evoke a mix of business and creativity
-Incorporate the color Gray or Black:White palette
-Open to see layouts in both vertical and horizontal
3 partners (we need 3 cards)
NORELLE VASK
ODA TRENCHARD
MARU ELDFORTH
Reason: We would like more submissions please
Target Market(s)
We are a NYC and European based boutique consulting agency specializing in fashion business and creative clients. In addition to consulting we will be offering an e-commerce site selling women’s accessories and jewelry geared towards fashion forward women ages 25-50.
Industry/Entity Type
Business
Font styles to use
Requirements
Must have
- - texture
- grayscale
3 Partners
Details for each card
CONSULTING I DESIGN
MARU ELDFORTH
Founding Partner
917.555.0183
maru@theplumwickhouse.com
www.theplumwickhouse.com
CONSULTING I DESIGN
NORELLE VASK
Founding Partner
917.555.0147
norelle@theplumwickhouse.com
www.theplumwickhouse.com
CONSULTING I DESIGN
Oda Kestlin Trenchard
Founding Partner
(no phone for her)
Oda@theplumwickhouse.com
www.theplumwickhouse.com

```html
<!DOCTYPE html>
<html lang="en">
<head>
<meta charset="utf-8">
<title>The Plumwick House — Business Cards</title>
<link rel="stylesheet" href="https://fonts.googleapis.com/css2?family=Josefin+Sans:wght@400&family=Arimo:wght@400&display=swap">
<style>
  :root {
    --page: #ffffff;
    --card: #333333;
    --rule: #6e6e6e;
    --ink: #ffffff;
  }
  html, body {
    margin: 0;
    width: 1200px;
    height: 1000px;
    overflow: hidden;
    background: var(--page);
  }
  .canvas { position: relative; width: 1200px; height: 1000px; }
  .card { position: absolute; width: 375px; height: 610px; display: block; }
  .card--front { left: 180px; top: 103px; }
  .card--back { left: 627px; top: 275px; }
  .card__bg { fill: var(--card); }
  .card__rule { fill: none; stroke: var(--rule); stroke-width: 2; }
  .wordmark {
    font-family: "Josefin Sans", sans-serif;
    font-size: 27px;
    letter-spacing: 5px;
    fill: var(--ink);
  }
  .tagline {
    font-family: "Arimo", sans-serif;
    font-size: 10px;
    letter-spacing: 3px;
    fill: var(--ink);
  }
  .contact__name { font-family: "Arimo", sans-serif; font-size: 16px; fill: var(--ink); }
  .contact__role { font-family: "Arimo", sans-serif; font-size: 13px; letter-spacing: 1px; fill: var(--ink); }
  .contact__line { font-family: "Arimo", sans-serif; font-size: 15px; fill: var(--ink); }
  .contact__icon { fill: none; stroke: var(--ink); stroke-width: 1.5; }
  .web { font-family: "Arimo", sans-serif; font-size: 12px; letter-spacing: 1.5px; fill: var(--ink); }
</style>
</head>
<body>
<main class="canvas">

  <svg class="card card--front" viewBox="0 0 375 610" aria-label="Business card front">
    <rect class="card__bg" width="375" height="610"/>
    <path class="card__rule" d="M250 0 V28 H347 V372 H375"/>
    <path class="card__rule" d="M0 236 H28 V582 H196 V610"/>
    <path class="card__rule" d="M60 396 H375"/>
    <path class="card__rule" d="M80 610 V540 H300 V520 H375"/>

    <g class="wordmark" text-anchor="middle">
      <text x="188" y="141">THE</text>
      <text x="188" y="181">PLUMWICK</text>
      <text x="188" y="221">HOUSE</text>
    </g>
    <text class="tagline" x="187" y="304" text-anchor="middle">CONSULTING I DESIGN</text>

    <text class="contact__name" x="98" y="432">MARU ELDFORTH</text>
    <text class="contact__role" x="98" y="449">Founding Partner</text>

    <rect class="contact__icon" x="105" y="462" width="10" height="18" rx="1.5"/>
    <line class="contact__icon" x1="105" y1="476" x2="115" y2="476"/>
    <text class="contact__line" x="127" y="476">917.555.0183</text>

    <rect class="contact__icon" x="99" y="488" width="21" height="14"/>
    <path class="contact__icon" d="M99 488 L109.5 497 L120 488"/>
    <text class="contact__line" x="127" y="499">maru@theplumwickhouse.com</text>
  </svg>

  <svg class="card card--back" viewBox="0 0 375 610" aria-label="Business card back">
    <rect class="card__bg" width="375" height="610"/>
    <path class="card__rule" d="M0 120 H140 V50 H280 V0"/>
    <path class="card__rule" d="M375 180 H230 V300"/>
    <path class="card__rule" d="M55 300 H320 V580 H55 Z"/>
    <path class="card__rule" d="M20 610 V230 H90 V300"/>

    <g class="wordmark" text-anchor="middle">
      <text x="188" y="363">THE</text>
      <text x="188" y="403">PLUMWICK</text>
      <text x="188" y="443">HOUSE</text>
    </g>
    <text class="web" x="187" y="543" text-anchor="middle">www.theplumwickhouse.com</text>
  </svg>

</main>
</body>
</html>
```